IT Company Business Card Design w/Stationary Design

We have a great logo we like! We are looking to redesign our business cards and all company logo'd merchandise/materials.

We are an IT Company located near the Bay Area (San Francisco, CA). We specialize in Managed Services and offer complete IT Computer and Network Support to Businesses of all sizes. We thrive on making a lasting impression. We have been doing IT for 15yrs+ but are young at heart. We like to stand out and be different. We want to be unique and have a recognizable brand. We need our logo to represent who we are. We are young, professional, creative and outstanding. We don't want to blend in, we want to stand out. Our business card needs to stand out and grab attention. Something Bold, yet simple and clean. (I will provide ideas of what we like to give a taste of what we are looking for).

The design can include any kind of texture/artistic design or sizing EXCEPT please "no square card designs" as they don't seem to fit in wallets very well. We dont mind curved edges, rounded corners, vertical layouts or horizontal layouts, embossing, letter press or raised surfaces. Again, we dont want to look average or plain or boring. :) Be creative - yet practical! We have ordered from Pebblecraft designs before and been very happy. Their card sizes tend to be a little different, so beware. Hope this helps!

Target Market(s)

Businesses - Small to Medium, Corporations, Publicly Traded Companies

Industry/Entity Type

Business

Contact Information for Business Card

Harbor Lantern IT
7318 Quillby Avenue
Suite F
Modesto, CA 95871

Office 209.555.0137
Direct 209.555.0182
Cell 209.555.0164

Ross Tavener
Founder, CEO
www.hlit-example.com
rtavener@hlit-example.com

Locations Serviced: Modesto, Stockton, Pleasanton, Fresno (incorporate this on the card ONLY if there's a good place to do so).

What we specialize in: Computer, Network, Voice, Data. (IT Services)

Our Logo Colors: Black and Blue (#006699). Open to using grey or orange as well - but not required. Don't want too busy....

Logo Font: "Cinthe" (Will attach logo font). We want type style to be clean. You can show different font types including our logo font - and we are open to other font ideas.

The logo can be separated. You can use elements together or apart. Surprise us! :) We "REALLY" want the "hl" to be our identifier/our brand people recognize.

Font styles to use
Sans Serif

Colors
0355a3
3176b5
f37122
f78f20
faa54b
474747
aaaaaa
757575
000000

Requirements
Must have
• Bold, Big, Colorful, Modern/yet Fun, Clean Design, Stand Out Presence, Texture would be welcomed - but not necessary, Card design shape can include cut corners or rounded or square edges. Be creative. (HOWEVER, we don't want a square design because we have found it doesn't fit in wallets that easily).
• We do like using Pebblecraft printing company (Which they have particular sizing on their card templates - beware), but are open to other design templates/printing companies as well. We just want to make sure its easy to find a print company to do our work. Too unique could be costly and hard to get cards printed.
• Colors to use: Our logo Blue (#006699), with either whites, grays, black, shades of our blue, and maybe a pinch of orange if needed. Primarily, blue, white, gray or black.
Nice to have
• Texture would be cool or little different edging or shape - but nothing too costly to print. I have seen cards with 3 sharp edges and one round edge. Something like that would be cool as an option. Or a vertical card.
• I love a faded watermark look. It would be nice to see some shading of our circle logo on a few designs. The circle with "hl" in it OR.... taking just the "hl" and using it alone.
Should not have
• No square card designs. Nothing too expensive or elaborate to print. No busy fonts. Do not like Times New Roman type fonts (too old looking). Not a lot of orange (if you even choose to use some orange).

```html
<!DOCTYPE html>
<html lang="en">
<head>
<meta charset="utf-8">
<title>Harbor Lantern IT – Business Card</title>
<link rel="stylesheet" href="https://fonts.googleapis.com/css2?family=Questrial&display=swap">
<style>
  :root {
    --backdrop: #1e1f21;
    --card: #3a3d41;
    --card-pattern-base: #34373b;
    --brand-blue: #2f86de;
    --pattern-blue: #2b7fd8;
    --ink-light: #f4f5f6;
    --ink-soft: #d9dbde;
  }
  * { box-sizing: border-box; margin: 0; padding: 0; }
  html, body {
    width: 1200px;
    height: 900px;
    overflow: hidden;
    background: var(--backdrop);
    font-family: "Questrial", sans-serif;
  }
  .canvas {
    width: 1200px;
    height: 900px;
    display: flex;
    align-items: center;
    justify-content: center;
    gap: 40px;
  }
  .card {
    position: relative;
    width: 540px;
    height: 353px;
    border-radius: 0 46px 0 0;
    overflow: hidden;
    box-shadow: 0 10px 28px rgba(0, 0, 0, 0.45);
  }
  .card-back {
    background: linear-gradient(135deg, var(--pattern-blue) 0%, var(--card-pattern-base) 55%, var(--pattern-blue) 100%);
  }
  .card-front {
    background: var(--card);
    color: var(--ink-light);
  }
  .contact {
    position: absolute;
    left: 34px;
    top: 78px;
    font-size: 14.5px;
    line-height: 1.32;
  }
  .contact-group + .contact-group { margin-top: 12px; }
  .contact-label {
    color: var(--brand-blue);
    font-size: 14.5px;
    letter-spacing: 0.3px;
  }
  .brand {
    position: absolute;
    right: 34px;
    top: 36px;
    width: 220px;
    display: flex;
    flex-direction: column;
    align-items: center;
  }
  .brand-dot {
    width: 118px;
    height: 118px;
    border-radius: 50%;
    background: var(--brand-blue);
  }
  .brand-name {
    margin-top: 14px;
    color: var(--ink-light);
    text-align: center;
    line-height: 1;
  }
  .brand-name-main {
    display: block;
    font-size: 40px;
    letter-spacing: 0.5px;
  }
  .brand-name-sub {
    display: block;
    margin-top: 4px;
    font-size: 22px;
    letter-spacing: 8px;
  }
  .person {
    position: absolute;
    right: 34px;
    bottom: 34px;
    width: 220px;
  }
  .person-name {
    font-size: 26px;
    letter-spacing: 1.5px;
    color: var(--ink-light);
  }
  .person-title {
    font-size: 13px;
    color: var(--ink-soft);
    margin-top: 2px;
  }
</style>
</head>
<body>
<main class="canvas">
  <section class="card card-back" role="img" aria-label="Card back: repeating blue lowercase monogram pattern on charcoal"></section>

  <section class="card card-front">
    <div class="contact">
      <div class="contact-group">
        <p class="contact-label">Phone</p>
        <p>Office 209.555.0137</p>
        <p>Direct 209.555.0182</p>
        <p>Cell 209.555.0164</p>
      </div>
      <div class="contact-group">
        <p class="contact-label">Address</p>
        <p>Harbor Lantern IT</p>
        <p>7318 Quillby Avenue,</p>
        <p>Suite F Modesto, CA 95871</p>
      </div>
      <div class="contact-group">
        <p class="contact-label">Web/E-mail</p>
        <p>www.hlit-example.com</p>
        <p>rtavener@hlit-example.com</p>
      </div>
    </div>

    <div class="brand">
      <div class="brand-dot"></div>
      <p class="brand-name">
        <span class="brand-name-main">harbor</span>
        <span class="brand-name-sub">lantern</span>
      </p>
    </div>

    <div class="person">
      <p class="person-name">Ross Tavener</p>
      <p class="person-title">Founder, CEO</p>
    </div>
  </section>
</main>
</body>
</html>
```